Business Card Design Project

Want a modern business card.
Concern is that our email address is long and thus poses a design challenge.
Items like the company name can be omitted from text as it will be available via the logo.

Example:
Desmond Farraway
President / CEO
Cell 555.304.2817
Office 555.619.0352
desmondf@qtvnetworkplatforms.example
www.qtvnetworkplatforms.example

Target Market(s)

Technical and executive level members of Information Technology companies in the Healthcare industry.

Industry/Entity Type

Business

Colors

Designer to choose colors to be used in the design.

Requirements
Nice to have
• Raised logo, but I am open.

```html
<!DOCTYPE html>
<html lang="en">
<head>
<meta charset="utf-8">
<title>QTV Network Platforms – Business Card</title>
<link rel="stylesheet" href="https://fonts.googleapis.com/css2?family=Lato:wght@400;700&display=swap">
<style>
  :root {
    --canvas: #e9e6e1;
    --card-black: #050505;
    --frame-white: #ffffff;
    --ink-white: #ffffff;
    --shadow: rgba(0,0,0,0.28);
  }
  * { box-sizing: border-box; margin: 0; padding: 0; }
  html, body { width: 1200px; height: 900px; overflow: hidden; }
  body {
    background: var(--canvas);
    font-family: "Lato", Arial, sans-serif;
    color: var(--ink-white);
    position: relative;
  }
  .card {
    position: absolute;
    left: 320px;
    width: 560px;
    height: 320px;
    box-shadow: 0 10px 24px var(--shadow);
  }
  /* Front */
  .card-front {
    top: 90px;
    background: var(--card-black);
    display: flex;
    align-items: center;
    justify-content: center;
  }
  .brand-name {
    font-weight: 700;
    font-size: 40px;
    letter-spacing: 2px;
    text-transform: uppercase;
    color: var(--ink-white);
    text-align: center;
    line-height: 1.15;
  }
  /* Back */
  .card-back {
    top: 470px;
    background: var(--frame-white);
    padding: 8px;
    display: grid;
    grid-template-columns: 1fr 1fr;
    grid-template-rows: 96px 1fr 1fr;
    gap: 6px;
  }
  .cell {
    background: var(--card-black);
    display: flex;
    flex-direction: column;
    align-items: center;
    justify-content: center;
    gap: 8px;
  }
  .cell-identity { grid-column: 1 / 3; justify-content: flex-end; padding-bottom: 12px; gap: 2px; }
  .person-name {
    font-weight: 700;
    font-size: 30px;
    letter-spacing: 0.5px;
    text-transform: uppercase;
  }
  .person-title { font-size: 17px; letter-spacing: 0.5px; }
  .contact-text { font-size: 15px; letter-spacing: 1px; }
  .contact-text.small { font-size: 13.5px; letter-spacing: 0.4px; }
  .icon { width: 44px; height: 44px; }
</style>
</head>
<body>
  <section class="card card-front" aria-label="Card front">
    <h1 class="brand-name">QTV Network<br>Platforms</h1>
  </section>

  <section class="card card-back" aria-label="Card back">
    <div class="cell cell-identity">
      <h2 class="person-name">Desmond Farraway</h2>
      <p class="person-title">President / CEO</p>
    </div>

    <div class="cell cell-mobile">
      <svg class="icon" viewBox="0 0 44 44" aria-hidden="true">
        <rect x="12" y="3" width="20" height="38" rx="3" fill="none" stroke="#fff" stroke-width="3"/>
        <rect x="15" y="8" width="14" height="22" fill="none" stroke="#fff" stroke-width="1.5"/>
        <circle cx="17" cy="35" r="1.6" fill="#fff"/>
        <circle cx="22" cy="35" r="1.6" fill="#fff"/>
        <circle cx="27" cy="35" r="1.6" fill="#fff"/>
      </svg>
      <p class="contact-text">555.304.2817</p>
    </div>

    <div class="cell cell-office">
      <svg class="icon" viewBox="0 0 44 44" aria-hidden="true">
        <path d="M10 6 l6 -2 l5 9 l-4 4 c2 5 5 8 10 10 l4 -4 l9 5 l-2 6 c-1 3 -4 4 -7 3 c-12 -4 -20 -12 -24 -24 c-1 -3 0 -6 3 -7z" fill="#fff"/>
      </svg>
      <p class="contact-text">555.619.0352</p>
    </div>

    <div class="cell cell-web">
      <svg class="icon" viewBox="0 0 44 44" aria-hidden="true">
        <g fill="none" stroke="#fff" stroke-width="2">
          <circle cx="22" cy="22" r="18"/>
          <ellipse cx="22" cy="22" rx="8" ry="18"/>
          <line x1="22" y1="4" x2="22" y2="40"/>
          <line x1="4" y1="22" x2="40" y2="22"/>
          <path d="M7 13 h30 M7 31 h30"/>
        </g>
      </svg>
      <p class="contact-text small">www.qtvnetworkplatforms.example</p>
    </div>

    <div class="cell cell-email">
      <svg class="icon" viewBox="0 0 44 44" aria-hidden="true">
        <path d="M4 18 L22 6 L40 18 V38 H4 Z" fill="#fff"/>
        <rect x="11" y="12" width="22" height="16" fill="#050505"/>
        <path d="M15 17 h14 M15 21 h14 M15 25 h10" stroke="#fff" stroke-width="1.5"/>
        <path d="M4 18 L22 30 L40 18" fill="none" stroke="#050505" stroke-width="2"/>
      </svg>
      <p class="contact-text small">desmondf@qtvnetworkplatforms.example</p>
    </div>
  </section>
</body>
</html>
```